Banner & also another minor digital image for an Online Academic Journal

A direct example of what I need can be found in this webpage: http://papers.tbhu-archive.org/qrvt/
(Please see attached files, "sAMPLE", and "sAMPLE 2", so you can see what I mean.)
This link (http://papers.tbhu-archive.org/qrvt/) is for an existing ONLINE ACADEMIC JOURNAL at the Thornbury Hill University.
It will help for you to be acquainted with the format of Online Academic Journals.
You will find that there is a banner on top as well as a digital image of a journal/book cover on the right.
I need a
(1) banner and
a (2) digital journal/book cover
for a website for an ONLINE ACADEMIC JOURNAL.
I am looking for a serious, professional, elegant design.
There will not be a print version. Only web-based online publication. No coding needed, only PSD, JPG/PNG and PDF.
1) We use PelloWave (http://archives.pellowave.com/repository-software/journals/) for the digital image of the journal/book cover layout. Link shows the general layout of the journal website.
2) For the digital image of the journal/book cover and also the banner,
Name of the journal is....
"Lumen: A Quarterly of Civic Ethics and Recovery Work"
Only this text will be used and applied to both banner and cover.
***The color associated with the theme of dignity is purple
****You could also add the color red.
*****I don't want the design to be garish, but accents in red might represent
the sexual exploitation and violence in the title.
3) Attached "sAmple 2" file is a basic design for the digital image of the journal/book cover from PelloWave. I am looking for something more elegant and professional looking. Your creativity is encouraged. I am open to receiving your interpretation.
Target Market(s)
Academics & Community Professionals
Industry/Entity Type
Non Profit
Contact Information for Business Card
Match journal design

```html
<!DOCTYPE html>
<html lang="en">
<head>
<meta charset="utf-8">
<title>Lumen — Banner and Cover</title>
<link rel="stylesheet" href="https://fonts.googleapis.com/css2?family=Ubuntu:wght@400;500&family=Ubuntu+Condensed&display=swap">
<style>
  :root {
    --violet-deep: #4417b0;
    --violet-mid: #5124bd;
    --violet-light: #7048cf;
    --haze: #b9a9e6;
    --title-white: #f6f3ff;
    --coral: #f2855c;
    --page: #ffffff;
  }
  * { margin: 0; padding: 0; box-sizing: border-box; }
  html, body {
    width: 1200px;
    height: 1200px;
    overflow: hidden;
    background: var(--page);
  }
  .canvas {
    position: relative;
    width: 1200px;
    height: 1200px;
  }

  /* Banner */
  .banner {
    position: absolute;
    left: 0; top: 0;
    width: 1200px; height: 140px;
    background: linear-gradient(90deg, var(--violet-deep) 0%, var(--violet-mid) 55%, var(--violet-light) 80%, var(--violet-mid) 100%);
    overflow: hidden;
  }
  .banner-title {
    position: absolute;
    left: 42px; top: 38px;
    font-family: "Ubuntu", sans-serif;
    font-weight: 500;
    font-size: 60px;
    line-height: 1;
    letter-spacing: 0.09em;
    color: var(--title-white);
  }
  .banner-subtitle {
    position: absolute;
    right: 334px; top: 49px;
    font-family: "Ubuntu Condensed", sans-serif;
    font-size: 21px;
    line-height: 26px;
    text-align: right;
    color: var(--coral);
    letter-spacing: 0.01em;
  }
  .banner-photo {
    position: absolute;
    right: 0; top: 0;
    width: 350px; height: 140px;
    background: radial-gradient(ellipse 60% 80% at 50% 55%, rgba(201,188,238,0.75) 0%, rgba(140,110,215,0.45) 55%, rgba(81,36,189,0) 100%);
  }

  /* Cover */
  .cover {
    position: absolute;
    left: 280px; top: 210px;
    width: 640px; height: 928px;
    background: linear-gradient(160deg, var(--violet-mid) 0%, var(--violet-deep) 60%, var(--violet-mid) 100%);
    overflow: hidden;
  }
  .cover-photo {
    position: absolute;
    right: 0; top: 0;
    width: 320px; height: 330px;
    background: radial-gradient(ellipse 65% 60% at 60% 45%, rgba(201,188,238,0.8) 0%, rgba(140,110,215,0.45) 55%, rgba(81,36,189,0) 100%);
  }
  .cover-title {
    position: absolute;
    left: 47px; top: 204px;
    font-family: "Ubuntu", sans-serif;
    font-weight: 500;
    font-size: 86px;
    line-height: 1;
    letter-spacing: 0.09em;
    color: var(--title-white);
  }
  .cover-subtitle {
    position: absolute;
    left: 47px; top: 312px;
    font-family: "Ubuntu Condensed", sans-serif;
    font-size: 29px;
    line-height: 38px;
    color: var(--coral);
    letter-spacing: 0.01em;
  }
</style>
</head>
<body>
<main class="canvas">
  <header class="banner">
    <h1 class="banner-title">LUMEN</h1>
    <p class="banner-subtitle">A QUARTERLY OF<br>CIVIC ETHICS AND RECOVERY WORK</p>
    <div class="banner-photo" role="img" aria-label="Soft violet-toned photograph of a figure covering their face with their hands"></div>
  </header>

  <section class="cover">
    <div class="cover-photo" role="img" aria-label="Soft violet-toned photograph of a figure with a hand held over their mouth"></div>
    <h2 class="cover-title">LUMEN</h2>
    <p class="cover-subtitle">A QUARTERLY OF<br>CIVIC ETHICS AND RECOVERY WORK</p>
  </section>
</main>
</body>
</html>
```